Wren Sporting Goods Inc.

Need to create a website that is informational and has the ability to sell goods and services. Such as a custom t shirt designer where the user can upload and image to be displayed on the garmet. The sports we specialize in are basketball, football, and baseball.

Would like like:
Home Page
Locker Room Page:
Custom Uniforms Page
Custom Shirt Creator
Brands
About

Competitor websites are
tundrafieldwearnx.com
dvq.com
lumarogear.com

```html
<!DOCTYPE html>
<html lang="en">
<head>
<meta charset="utf-8">
<title>Wren Sporting Goods — Design Your Team</title>
<link href="https://fonts.googleapis.com/css2?family=Urbanist:wght@400;500;600;700&family=Poppins:wght@400;500;600&display=swap" rel="stylesheet">
<style>
:root{
  --bg:#f6f6f6;
  --ink:#111111;
  --muted:#555555;
  --red:#dc3a2e;
  --blue:#1f5fc6;
  --card:#ffffff;
  --dark:#0b0b0b;
  --line:#d9d9d9;
}
*{box-sizing:border-box;margin:0;padding:0}
html,body{width:1200px;height:5319px;overflow:hidden}
body{position:relative;background:var(--bg);font-family:"Poppins",sans-serif;color:var(--ink)}
.abs{position:absolute}
.heading{font-family:"Urbanist",sans-serif;font-weight:500;color:var(--ink);letter-spacing:-0.5px}
.btn{position:absolute;display:flex;align-items:center;justify-content:center;font-size:11px;font-weight:500;color:#fff;background:var(--red);border-radius:3px;box-shadow:0 3px 6px rgba(0,0,0,.18)}
.btn.ghost{background:#e2e2e2;color:#999}
.btn.pill{background:#fff;color:#222;border:1px solid #aaa;border-radius:14px;box-shadow:none;font-size:8px}
.ph{position:absolute;border-radius:6px}
.shadow{box-shadow:0 6px 20px rgba(0,0,0,.12)}
.brand{font-family:"Urbanist",sans-serif;font-weight:700;color:var(--blue);font-size:22px;line-height:1;display:flex;align-items:center;gap:8px}
.brand .mark{width:14px;height:14px;background:var(--red);border-radius:50%}
.nav-links{display:flex;gap:26px;font-size:11px;color:#222}
.pcard{position:absolute;background:var(--card);border-radius:10px}
.pcard .name{position:absolute;width:100%;text-align:center;font-family:"Urbanist",sans-serif;font-weight:700;font-size:15px}
.pcard .sub{position:absolute;width:100%;text-align:center;font-size:8px;color:#666}
.arrow-circle{position:absolute;width:30px;height:30px;border-radius:50%;background:#fff;box-shadow:0 2px 6px rgba(0,0,0,.2);display:flex;align-items:center;justify-content:center}
.stat .num{font-family:"Urbanist",sans-serif;font-size:36px;font-weight:500}
.stat .lbl{font-size:9px;color:#444;margin-top:6px}
.step{position:absolute;width:48px;height:48px;border-radius:50%;background:#fff;box-shadow:0 3px 10px rgba(0,0,0,.15);display:flex;align-items:center;justify-content:center;font-family:"Urbanist",sans-serif;font-weight:700;font-size:28px}
.upcard{position:absolute;background:#fff;border-radius:8px;box-shadow:0 6px 20px rgba(0,0,0,.12);padding:28px}
.upcard h4{font-family:"Poppins",sans-serif;font-size:14px;font-weight:600;margin-top:22px}
.upcard p{font-size:8.5px;color:#555;line-height:1.9;margin-top:14px}
.prod{position:absolute;width:262px;height:336px;background:#fff;border:1px solid #ddd}
.prod .band{position:absolute;left:0;bottom:0;width:100%;height:80px;background:#0d0d0d;color:#fff;padding:8px 8px}
.prod.hot .band{background:#d8493d}
.prod .band h5{font-family:"Urbanist",sans-serif;font-weight:600;font-size:17px}
.prod .band .tiny{font-size:6px;line-height:1.5;color:#ddd;margin-top:4px;width:150px}
.prod .band .price{font-size:10px;margin-top:6px}
.prod .band .price s{font-size:7px;color:#bbb;margin-left:8px}
.prod .plus{position:absolute;right:14px;top:20px;width:36px;height:36px;border-radius:50%;background:#fff;color:#111;display:flex;align-items:center;justify-content:center;font-size:24px;font-weight:300}
.prod.hot .plus{background:#111;color:#fff}
.prod .shot{position:absolute;left:30px;top:14px;width:200px;height:222px;border-radius:6px}
.side-arrow{position:absolute;width:32px;height:56px;background:var(--blue);display:flex;align-items:center;justify-content:center}
.fcard{position:absolute;width:267px;height:330px;background:#fff;border-radius:6px;box-shadow:0 8px 24px rgba(0,0,0,.14);text-align:center;padding-top:34px}
.fcard h4{font-size:14px;font-weight:600;line-height:1.7;margin-top:22px}
.fcard p{font-size:8.5px;color:#555;line-height:1.9;margin:16px 34px 0}
.fcard .pill{position:relative;margin:16px auto 0;width:92px;height:18px}
.tcard{position:absolute;width:246px;height:303px;background:#fff;border-radius:8px;box-shadow:0 6px 20px rgba(0,0,0,.12)}
.tcard .nm{position:absolute;left:28px;font-family:"Urbanist",sans-serif;font-weight:600;font-size:14px}
.tcard .role{position:absolute;left:28px;font-size:8px;color:#666}
.tcard .stars{color:#111;font-size:11px;letter-spacing:2px}
.tcard h5{font-size:13px;font-weight:600;line-height:1.3;margin-top:6px}
.tcard p{font-size:7.5px;color:#555;line-height:2;margin-top:10px}
footer{position:absolute;left:0;top:4878px;width:1200px;height:441px;background:var(--dark);color:#fff;overflow:hidden}
.fcol{position:absolute;top:173px;font-size:9px;color:#ddd;line-height:2.6}
.fcol h6{font-size:9px;font-weight:600;color:#fff;margin-bottom:12px;line-height:1}
.watermark{position:absolute;left:0;top:262px;font-family:"Urbanist",sans-serif;font-weight:700;font-size:230px;color:#1c1c1c;letter-spacing:6px;line-height:1}
</style>
</head>
<body>

<header>
  <div class="brand abs" style="left:150px;top:24px">Wren Sporting Goods<span class="mark"></span></div>
  <nav class="nav-links abs" style="left:413px;top:30px">
    <span>Home</span><span>Locker Room</span><span>Custom Uniforms</span><span>Custom Shirt</span><span>Brands</span><span>About</span>
  </nav>
  <div class="btn" style="left:937px;top:20px;width:112px;height:38px">Sign In/Up</div>
</header>

<section class="hero">
  <svg class="abs" style="left:0;top:0" width="1200" height="720" aria-hidden="true">
    <polygon points="1200,52 1200,470 352,640 345,628" fill="var(--blue)"/>
  </svg>
  <div class="ph" role="img" aria-label="Red and blue football jersey" style="left:733px;top:62px;width:341px;height:413px;background:radial-gradient(ellipse at 50% 45%,#b22a4e 0%,#3b2a7a 55%,rgba(31,95,198,0) 80%);border-radius:16px"></div>
  <h1 class="heading abs" style="left:147px;top:134px;font-size:62px;line-height:72px">Design Your Team<br>Wear Your Pride</h1>
  <p class="abs" style="left:147px;top:290px;font-size:11px;line-height:19px;color:#333;width:450px">Introduction to your brand, sports specialization (basketball, football, baseball), highlight customization feature</p>
  <div class="btn" style="left:147px;top:363px;width:136px;height:36px">Start Designing</div>
  <div class="btn ghost" style="left:300px;top:363px;width:103px;height:36px">Shop Now</div>

  <div class="pcard shadow" style="left:157px;top:467px;width:190px;height:227px">
    <div class="ph" role="img" aria-label="Blue football shirt" style="left:27px;top:14px;width:136px;height:148px;background:linear-gradient(160deg,#2a6ee8,#1346b8)"></div>
    <div class="name" style="top:176px">Football</div>
    <div class="sub" style="top:198px">Tech Wear</div>
  </div>
  <div class="arrow-circle" style="left:153px;top:664px"><svg width="12" height="12"><path d="M2 10 L10 2 M4 2 H10 V8" stroke="#222" stroke-width="1.5" fill="none"/></svg></div>

  <div class="pcard shadow" style="left:396px;top:467px;width:195px;height:227px">
    <div class="ph" role="img" aria-label="Black and red baseball shirt" style="left:27px;top:14px;width:141px;height:148px;background:linear-gradient(160deg,#c4252d,#1a1a1a 70%)"></div>
    <div class="name" style="top:176px">Baseball</div>
    <div class="sub" style="top:198px">Street Wear</div>
  </div>
  <div class="arrow-circle" style="left:392px;top:664px"><svg width="12" height="12"><path d="M2 10 L10 2 M4 2 H10 V8" stroke="#222" stroke-width="1.5" fill="none"/></svg></div>

  <div class="pcard shadow" style="left:628px;top:491px;width:435px;height:190px;background:#eeeeee">
    <div class="ph" role="img" aria-label="Row of black basketball team t-shirts" style="left:20px;top:20px;width:395px;height:150px;background:linear-gradient(90deg,#1b1b1b,#2d2a24 50%,#1b1b1b)"></div>
    <div class="abs" style="left:197px;top:75px;width:40px;height:40px;border-radius:50%;background:rgba(255,255,255,.35);display:flex;align-items:center;justify-content:center">
      <svg width="14" height="14"><polygon points="3,1 13,7 3,13" fill="#fff"/></svg>
    </div>
  </div>
</section>

<section class="needs">
  <svg class="abs" style="left:0;top:860px" width="140" height="380" aria-hidden="true">
    <polygon points="0,8 135,140 135,310 0,360" fill="var(--blue)"/>
  </svg>
  <div class="ph" role="img" aria-label="Padel player in white team shirt on court" style="left:130px;top:826px;width:461px;height:473px;background:linear-gradient(135deg,#5e4a3c,#9a8676 45%,#2f3a34);border-radius:10px"></div>
  <h2 class="heading abs" style="left:613px;top:890px;font-size:50px;line-height:58px">Everything Your<br>Team Needs</h2>
  <p class="abs" style="left:613px;top:1022px;width:420px;font-size:11px;line-height:20px;color:#333">Showcases all products, accessories, and gear offered. Could include team packages or sports categories</p>
  <div class="btn" style="left:613px;top:1097px;width:130px;height:33px">View Products</div>
  <div class="stat abs" style="left:613px;top:1166px"><div class="num">3.2M+</div><div class="lbl">Outfits Generated</div></div>
  <div class="stat abs" style="left:795px;top:1166px"><div class="num">12M+</div><div class="lbl">Outfits Generated</div></div>
  <div class="stat abs" style="left:964px;top:1166px"><div class="num">98%</div><div class="lbl">Satisfaction Rate</div></div>
</section>

<section class="steps">
  <h2 class="heading abs" style="left:0;top:1394px;width:1200px;text-align:center;font-size:45px">Your Team, Your Design</h2>
  <p class="abs" style="left:410px;top:1458px;width:380px;text-align:center;font-size:11px;line-height:20px;color:#333">Simple, intuitive, and crafted to make daily styling fun and stress-free.</p>
  <svg class="abs" style="left:0;top:1575px" width="1200" height="4" aria-hidden="true"><line x1="250" y1="2" x2="955" y2="2" stroke="#222" stroke-width="1.5" stroke-dasharray="10 8"/></svg>
  <div class="step" style="left:199px;top:1552px">1</div>
  <div class="step" style="left:575px;top:1552px">2</div>
  <div class="step" style="left:953px;top:1552px">3</div>

  <div class="upcard" style="left:151px;top:1652px;width:243px;height:252px">
    <svg width="104" height="104" viewBox="0 0 52 52" aria-hidden="true"><rect x="3" y="8" width="38" height="38" rx="3" fill="none" stroke="#111" stroke-width="3.5"/><polygon points="9,40 19,27 26,34 31,29 37,40" fill="#111"/><path d="M40 3 V17 M33 10 H47" stroke="#111" stroke-width="3.5"/></svg>
    <h4>Upload Your image</h4>
    <p>Lorem ipsum dolor sit amet, consectetur adipiscing elit. Quisque non mollis purus.</p>
  </div>
  <div class="upcard" style="left:477px;top:1652px;width:246px;height:252px">
    <svg width="104" height="104" viewBox="0 0 52 52" aria-hidden="true"><rect x="3" y="8" width="38" height="38" rx="3" fill="none" stroke="#111" stroke-width="3.5"/><polygon points="9,40 19,27 26,34 31,29 37,40" fill="#111"/><path d="M40 3 V17 M33 10 H47" stroke="#111" stroke-width="3.5"/></svg>
    <h4>Upload Your image</h4>
    <p>Lorem ipsum dolor sit amet, consectetur adipiscing elit. Quisque non mollis purus.</p>
  </div>
  <div class="upcard" style="left:805px;top:1652px;width:244px;height:252px">
    <svg width="104" height="104" viewBox="0 0 52 52" aria-hidden="true"><rect x="3" y="8" width="38" height="38" rx="3" fill="none" stroke="#111" stroke-width="3.5"/><polygon points="9,40 19,27 26,34 31,29 37,40" fill="#111"/><path d="M40 3 V17 M33 10 H47" stroke="#111" stroke-width="3.5"/></svg>
    <h4>Upload Your image</h4>
    <p>Lorem ipsum dolor sit amet, consectetur adipiscing elit. Quisque non mollis purus.</p>
  </div>
  <div class="btn" style="left:516px;top:1945px;width:170px;height:33px">Create Your Uniform</div>
</section>

<section class="brands">
  <h2 class="heading abs" style="left:0;top:2072px;width:1200px;text-align:center;font-size:45px">Quality Brands We Trust</h2>
  <p class="abs" style="left:335px;top:2136px;width:530px;text-align:center;font-size:11px;line-height:20px;color:#333">Highlight brands and suppliers used for uniforms and shirts (like Stridewell, Korvane, Halden Gear).</p>

  <div class="side-arrow" style="left:151px;top:2541px"><svg width="16" height="12"><path d="M15 6 H2 M7 1 L2 6 L7 11" stroke="#fff" stroke-width="1.6" fill="none"/></svg></div>
  <div class="side-arrow" style="left:1014px;top:2541px"><svg width="16" height="12"><path d="M1 6 H14 M9 1 L14 6 L9 11" stroke="#fff" stroke-width="1.6" fill="none"/></svg></div>

  <div class="prod hot" style="left:186px;top:2226px">
    <div class="shot" role="img" aria-label="Navy, red and white printed football shirt" style="background:linear-gradient(160deg,#1f2e6e,#c33 50%,#eee)"></div>
    <div class="band"><h5>Football T-Shirt</h5><div class="tiny">Light breathable mesh, sewn team numbers and crest</div><div class="price">$7.99<s>$9.99</s></div><div class="plus">+</div></div>
  </div>
  <div class="prod" style="left:469px;top:2226px">
    <div class="shot" role="img" aria-label="White baseball jersey" style="background:linear-gradient(160deg,#f4f4f4,#d6d9e6)"></div>
    <div class="band"><h5>Baseball T-Shirt</h5><div class="tiny">Light breathable mesh, sewn team numbers and crest</div><div class="price">$7.99<s>$9.99</s></div><div class="plus">+</div></div>
  </div>
  <div class="prod" style="left:752px;top:2226px">
    <div class="shot" role="img" aria-label="Black basketball jersey with yellow trim" style="background:linear-gradient(160deg,#2a2a2a,#141414 70%,#c9b23a)"></div>
    <div class="band"><h5>Basketball T-Shirt</h5><div class="tiny">Light breathable mesh, sewn team numbers and crest</div><div class="price">$7.99<s>$9.99</s></div><div class="plus">+</div></div>
  </div>
  <div class="prod" style="left:186px;top:2579px">
    <div class="shot" role="img" aria-label="Navy polo shirt with red side panels" style="background:linear-gradient(160deg,#1d2750,#2b376a 70%,#b22)"></div>
    <div class="band"><h5>Baseball T-Shirt</h5><div class="tiny">Light breathable mesh, sewn team numbers and crest</div><div class="price">$7.99<s>$9.99</s></div><div class="plus">+</div></div>
  </div>
  <div class="prod" style="left:469px;top:2579px">
    <div class="shot" role="img" aria-label="Red and white sports shirt" style="background:linear-gradient(160deg,#d81e2a,#f3f3f3 60%)"></div>
    <div class="band"><h5>Baseball T-Shirt</h5><div class="tiny">Light breathable mesh, sewn team numbers and crest</div><div class="price">$7.99<s>$9.99</s></div><div class="plus">+</div></div>
  </div>
  <div class="prod" style="left:752px;top:2579px">
    <div class="shot" role="img" aria-label="Navy and gold rugby shirt" style="background:linear-gradient(160deg,#1c2550,#e2b128 60%,#1c2550)"></div>
    <div class="band"><h5>Basketball T-Shirt</h5><div class="tiny">Light breathable mesh, sewn team numbers and crest</div><div class="price">$7.99<s>$9.99</s></div><div class="plus">+</div></div>
  </div>
  <div class="btn" style="left:533px;top:2953px;width:138px;height:33px">View All Product</div>
</section>

<section class="features">
  <h2 class="heading abs" style="left:151px;top:3082px;font-size:50px;line-height:58px">Upload. Customize.<br>Wear</h2>
  <p class="abs" style="left:785px;top:3087px;width:270px;font-size:11px;line-height:20px;color:#333">Our platform helps you save time, express yourself, and make the most of every outfit you own.</p>
  <div class="btn" style="left:785px;top:3166px;width:153px;height:33px">Design Your Shirt</div>

  <svg class="abs" style="left:0;top:3300px" width="1200" height="860" aria-hidden="true">
    <polygon points="1200,10 1200,330 900,420" fill="var(--blue)"/>
    <polygon points="0,470 470,850 0,850" fill="var(--blue)"/>
  </svg>
  <div class="ph" role="img" aria-label="Two orange custom jerseys showing name, number and logo placement" style="left:620px;top:3304px;width:495px;height:361px;background:linear-gradient(135deg,#e2551c,#f07a23 50%,#e84c1a);border-radius:12px"></div>
  <div class="ph" role="img" aria-label="Red and black football jersey" style="left:62px;top:3748px;width:403px;height:392px;background:linear-gradient(150deg,#c01a22,#5a1216 55%,#151515);border-radius:12px"></div>

  <div class="fcard" style="left:101px;top:3273px">
    <svg width="104" height="104" viewBox="0 0 52 52" aria-hidden="true"><rect x="3" y="8" width="38" height="38" rx="3" fill="none" stroke="#111" stroke-width="3.5"/><polygon points="9,40 19,27 26,34 31,29 37,40" fill="#111"/><path d="M40 3 V17 M33 10 H47" stroke="#111" stroke-width="3.5"/></svg>
    <h4>Maximizes outfit<br>combinations</h4>
    <p>Lorem ipsum dolor sit amet, consectetur adipiscing elit. Quisque non mollis purus.</p>
    <div class="btn pill">Learn More</div>
  </div>
  <div class="fcard" style="left:343px;top:3459px">
    <svg width="104" height="104" viewBox="0 0 52 52" aria-hidden="true"><rect x="3" y="8" width="38" height="38" rx="3" fill="none" stroke="#111" stroke-width="3.5"/><polygon points="9,40 19,27 26,34 31,29 37,40" fill="#111"/><path d="M40 3 V17 M33 10 H47" stroke="#111" stroke-width="3.5"/></svg>
    <h4>Keeps your<br>wardrobe organized</h4>
    <p>Lorem ipsum dolor sit amet, consectetur adipiscing elit. Quisque non mollis purus.</p>
    <div class="btn pill">Learn More</div>
  </div>
  <div class="fcard" style="left:586px;top:3645px">
    <svg width="104" height="104" viewBox="0 0 52 52" aria-hidden="true"><rect x="3" y="8" width="38" height="38" rx="3" fill="none" stroke="#111" stroke-width="3.5"/><polygon points="9,40 19,27 26,34 31,29 37,40" fill="#111"/><path d="M40 3 V17 M33 10 H47" stroke="#111" stroke-width="3.5"/></svg>
    <h4>Saves time<br>planning daily looks</h4>
    <p>Lorem ipsum dolor sit amet, consectetur adipiscing elit. Quisque non mollis purus.</p>
    <div class="btn pill">Learn More</div>
  </div>
  <div class="fcard" style="left:832px;top:3820px">
    <svg width="104" height="104" viewBox="0 0 52 52" aria-hidden="true"><rect x="3" y="8" width="38" height="38" rx="3" fill="none" stroke="#111" stroke-width="3.5"/><polygon points="9,40 19,27 26,34 31,29 37,40" fill="#111"/><path d="M40 3 V17 M33 10 H47" stroke="#111" stroke-width="3.5"/></svg>
    <h4>Helps reduce<br>fashion waste</h4>
    <p>Lorem ipsum dolor sit amet, consectetur adipiscing elit. Quisque non mollis purus.</p>
    <div class="btn pill">Learn More</div>
  </div>
</section>

<section class="reviews">
  <h2 class="heading abs" style="left:0;top:4247px;width:1200px;text-align:center;font-size:45px">What Our Users Say</h2>
  <p class="abs" style="left:410px;top:4314px;width:380px;text-align:center;font-size:11px;line-height:20px;color:#333">Real stories from people who transformed their daily styling experience.</p>

  <div class="tcard" style="left:68px;top:4405px">
    <div class="ph" role="img" aria-label="Customer wearing a white team shirt" style="left:28px;top:26px;width:190px;height:200px;background:linear-gradient(160deg,#cfd3d6,#7d8a70)"></div>
    <div class="nm" style="top:240px">Dana Whitfield</div>
    <div class="role" style="top:262px">Fashion Student</div>
  </div>
  <div class="tcard" style="left:339px;top:4405px;padding:26px 28px">
    <div style="display:flex;align-items:center;gap:10px">
      <div role="img" aria-label="Customer portrait" style="width:36px;height:36px;border-radius:50%;background:#b59a84"></div>
      <div><div style="font-size:9px;font-weight:600">Maren Holt</div><div style="font-size:6px;color:#777">Corporate Consultant</div></div>
    </div>
    <div class="stars" style="margin-top:12px">★★★★★</div>
    <h5>My wardrobe feels<br>new again!</h5>
    <p>"I used to think I needed more clothes, but the app helped me rediscover what I already own. The combinations it suggests are creative and stylish. It's like having a personal stylist who knows my closet better than I do."</p>
  </div>
  <div class="tcard" style="left:613px;top:4405px">
    <div class="ph" role="img" aria-label="Customer in a black custom jersey" style="left:28px;top:26px;width:190px;height:200px;background:linear-gradient(160deg,#2c3035,#111 70%,#c7731f)"></div>
    <div class="nm" style="top:240px">Cool Priya</div>
    <div class="role" style="top:262px">Fashion Teacher</div>
  </div>
  <div class="tcard" style="left:886px;top:4405px;padding:26px 28px">
    <div style="display:flex;align-items:center;gap:10px">
      <div role="img" aria-label="Customer portrait" style="width:36px;height:36px;border-radius:50%;background:#d9b9a6"></div>
      <div><div style="font-size:9px;font-weight:600">Tessa R.</div><div style="font-size:6px;color:#777">Digital Marketer &amp; Content Creator</div></div>
    </div>
    <div class="stars" style="margin-top:12px">★★★★★</div>
    <h5>I save 20 minutes<br>every morning.</h5>
    <p>"The app puts together outfits faster than I ever could. No more staring at my closet wondering what to wear — everything is ready, coordinated, and tailored to the weather. It's honestly made my mornings so much smoother."</p>
  </div>

  <div class="abs" style="left:550px;top:4746px;width:32px;height:32px;border-radius:50%;background:#fff;box-shadow:0 2px 6px rgba(0,0,0,.2);display:flex;align-items:center;justify-content:center"><svg width="10" height="10"><path d="M7 1 L3 5 L7 9" stroke="#222" stroke-width="1.4" fill="none"/></svg></div>
  <div class="abs" style="left:618px;top:4746px;width:32px;height:32px;border-radius:50%;background:var(--red);box-shadow:0 2px 6px rgba(0,0,0,.2);display:flex;align-items:center;justify-content:center"><svg width="10" height="10"><path d="M3 1 L7 5 L3 9" stroke="#fff" stroke-width="1.4" fill="none"/></svg></div>
</section>

<footer>
  <div class="watermark">SPORTING</div>
  <div class="brand abs" style="left:157px;top:60px;font-size:30px">Wren Sporting Goods<span class="mark" style="width:18px;height:18px"></span></div>
  <div class="abs" style="left:714px;top:64px;width:42px;height:42px;border:1px solid #fff;border-radius:50%;display:flex;align-items:center;justify-content:center">
    <svg width="16" height="12"><rect x="1" y="1" width="14" height="10" rx="1" fill="none" stroke="#fff" stroke-width="1.2"/><path d="M1 2 L8 7 L15 2" stroke="#fff" stroke-width="1.2" fill="none"/></svg>
  </div>
  <div class="abs" style="left:768px;top:64px;width:281px;height:42px;border:1px solid #fff;border-radius:21px;display:flex;align-items:center;justify-content:space-between;padding:0 20px;font-size:10px;color:#ddd">
    <span>Enter Your Email...</span>
    <svg width="14" height="12"><polygon points="1,1 13,6 1,11 3,6" fill="#fff"/></svg>
  </div>
  <div class="abs" style="left:151px;top:136px;width:898px;height:1px;background:#444"></div>

  <div class="fcol" style="left:171px"><h6>Quick links</h6>Home<br>Locker Room<br>Custom Uniforms<br>Custom Shirt<br>Brands<br>About</div>
  <div class="fcol" style="left:345px"><h6>Payment</h6>Bank<br>Paywisp<br>Qodex</div>
  <div class="fcol" style="left:491px"><h6>Follow Us</h6>Snapgrid<br>Circlebook<br>Chatterly</div>
  <div class="fcol" style="left:774px;line-height:1.8"><h6>Contact</h6>412 Birchline Rd. Dover Falls,<br>Ohio 40218<br><span style="font-weight:600;color:#fff">Office</span><br>88 Kestrel Way, Pine Hollow, Oregon 97022</div>
  <div class="fcol" style="left:956px"><h6>Phone Number</h6>(555) 014-2290</div>
</footer>

</body>
</html>
```